Hi,

I have just started up a business called VOLMIRA in Melbourne. We run fun street art tours around Melbourne's CBD.

I need to create a design for the back side of my business cards. I have designed the front side (simply with my logo) however, I am having trouble designing the reverse side in a professional manner. I have attached pictures of what I have done.

The picture attached titled "VOLMIRA Business Cards Back" has all the information that I require on the back side of my business cards; although displayed in an amateur and simple way. As displayed in the picture, I need: the VOLMIRA logo, the website URL, the booking details (phone - 0468 152 837 & email - bookings@volmira-example.com.au) and the service description ($20, One Hour, Tours Daily, Meet at Halberton St Station). I would also like to use the font in the picture supplied which is "source-sans-pro".

The VOLMIRA tours are for tourists and are relaxed, entertaining and fun! I would like the design to reflect this.

Target Market(s)

Backpackers & University Students

Industry/Entity Type

Business

Requirements
Must have
• The VOLMIRA logo, the website URL, the booking details (phone - 0468 152 837 & email - bookings@volmira-example.com.au) and the service description ($20, One Hour, Tours Daily, Meet at Halberton St Station).

```html
<!DOCTYPE html>
<html lang="en">
<head>
<meta charset="utf-8">
<title>VOLMIRA Business Cards</title>
<link rel="stylesheet" href="https://fonts.googleapis.com/css2?family=Source+Sans+3:wght@400;600;700;900&family=Tinos:wght@700&display=swap">
<style>
  :root {
    --backdrop: #2b2b2b;
    --backdrop-edge: #141414;
    --paper: #e9e7e8;
    --ink: #151515;
    --night: #050505;
    --spray-red: #f0574a;
    --ribbon-red: #e3262b;
    --ribbon-shade: #b81d22;
    --headline-red: #e4584a;
    --divider: #cfcfcf;
    --soft-white: #f2f2f2;
  }
  * { box-sizing: border-box; margin: 0; padding: 0; }
  html, body { width: 1200px; height: 1200px; overflow: hidden; }
  body {
    background: radial-gradient(circle at 50% 40%, var(--backdrop) 0%, var(--backdrop-edge) 100%);
    font-family: "Source Sans 3", "Source Sans Pro", sans-serif;
    position: relative;
  }
  .card {
    position: absolute;
    left: 160px;
    width: 880px;
    height: 500px;
    overflow: hidden;
    box-shadow: 0 18px 40px rgba(0,0,0,.55);
  }
  .card--front { top: 90px; background: var(--paper); }
  .card--back { top: 630px; display: flex; }

  .brand {
    display: flex;
    align-items: center;
    gap: 18px;
    color: var(--ink);
    font-weight: 900;
    letter-spacing: 2px;
    white-space: nowrap;
  }
  .brand__dot {
    border-radius: 50%;
    background: var(--spray-red);
    flex: none;
  }

  .front__brand {
    position: absolute;
    left: 200px; top: 120px;
    font-size: 96px;
  }
  .front__brand .brand__dot { width: 64px; height: 64px; }
  .front__tagline {
    position: absolute;
    left: 0; right: 0; top: 290px;
    text-align: center;
    font-size: 52px;
    font-weight: 700;
    line-height: 1.05;
    color: var(--ink);
  }

  .back__contact {
    width: 47%;
    background: var(--paper);
    position: relative;
  }
  .back__brand {
    position: absolute;
    left: 56px; top: 95px;
    font-size: 64px;
  }
  .back__brand .brand__dot { width: 44px; height: 44px; }
  .contact-list {
    position: absolute;
    left: 28px; bottom: 48px;
    list-style: none;
    display: flex;
    flex-direction: column;
    gap: 16px;
  }
  .contact-list li {
    display: flex;
    align-items: center;
    gap: 12px;
    font-size: 19px;
    font-weight: 700;
    color: var(--ink);
    white-space: nowrap;
  }
  .contact-list svg { width: 30px; height: 30px; flex: none; }

  .back__divider {
    width: 18px;
    background: var(--divider);
    border-left: 6px solid var(--soft-white);
    border-right: 6px solid var(--night);
  }
  .back__offer {
    flex: 1;
    background: var(--night);
    position: relative;
    color: var(--soft-white);
  }
  .offer__headline {
    position: absolute;
    left: 20px; right: 20px; top: 50px;
    font-family: "Tinos", "Times New Roman", serif;
    font-weight: 700;
    font-size: 34px;
    line-height: 1.08;
    color: var(--headline-red);
    text-align: center;
    white-space: nowrap;
  }
  .price-badge {
    position: absolute;
    right: 36px; top: 140px;
    width: 110px; height: 120px;
  }
  .offer-list {
    position: absolute;
    left: 36px; bottom: 55px;
    list-style: none;
    display: flex;
    flex-direction: column;
    gap: 16px;
  }
  .offer-list li {
    display: flex;
    align-items: center;
    gap: 16px;
    font-size: 26px;
    font-weight: 600;
    white-space: nowrap;
  }
  .offer-list svg { width: 28px; height: 28px; flex: none; }
</style>
</head>
<body>

<section class="card card--front" aria-label="Business card front">
  <div class="brand front__brand"><span class="brand__dot"></span>VOLMIRA</div>
  <p class="front__tagline">Melbourne Street Art<br>Walking Tours</p>
</section>

<section class="card card--back" aria-label="Business card back">
  <div class="back__contact">
    <div class="brand back__brand"><span class="brand__dot"></span>VOLMIRA</div>
    <ul class="contact-list">
      <li>
        <svg viewBox="0 0 32 32" aria-hidden="true"><circle cx="16" cy="16" r="15" fill="var(--ribbon-red)"/><path d="M11 9c1-1 2-1 3 0l1 3c0 1-1 1-1 2 1 2 2 3 4 4 1 0 1-1 2-1l3 1c1 1 1 2 0 3-2 2-5 1-8-2s-5-7-4-10z" fill="#fff"/></svg>
        <span>0468 152 837</span>
      </li>
      <li>
        <svg viewBox="0 0 32 32" aria-hidden="true"><circle cx="16" cy="16" r="15" fill="var(--ribbon-red)"/><rect x="8" y="11" width="16" height="11" fill="none" stroke="#fff" stroke-width="2"/><path d="M8 11l8 6 8-6" fill="none" stroke="#fff" stroke-width="2"/></svg>
        <span>bookings@volmira-example.com.au</span>
      </li>
      <li>
        <svg viewBox="0 0 32 32" aria-hidden="true"><circle cx="16" cy="16" r="15" fill="var(--ribbon-red)"/><g fill="none" stroke="#fff" stroke-width="1.6"><circle cx="16" cy="16" r="8"/><ellipse cx="16" cy="16" rx="3.5" ry="8"/><path d="M8 16h16M9.5 12h13M9.5 20h13"/></g></svg>
        <span>www.volmira-example.com.au</span>
      </li>
    </ul>
  </div>

  <div class="back__divider"></div>

  <div class="back__offer">
    <h2 class="offer__headline">Melbourne Street Art<br>Walking Tours</h2>
    <svg class="price-badge" viewBox="0 0 120 130" role="img" aria-label="Price $20">
      <path d="M38 50 L20 118 L34 108 L44 124 L60 60 Z" fill="var(--ribbon-red)"/>
      <path d="M70 52 L108 112 L92 110 L90 126 L56 64 Z" fill="var(--ribbon-shade)"/>
      <polygon fill="var(--ribbon-red)" points="60,4 66,14 77,9 79,21 91,21 88,33 99,38 91,47 99,56 88,61 91,73 79,73 77,85 66,80 60,90 54,80 43,85 41,73 29,73 32,61 21,56 29,47 21,38 32,33 29,21 41,21 43,9 54,14"/>
      <text x="60" y="56" text-anchor="middle" font-family="Source Sans 3, sans-serif" font-weight="700" font-size="26" fill="#fff">$20</text>
    </svg>
    <ul class="offer-list">
      <li><svg viewBox="0 0 28 28" aria-hidden="true"><circle cx="14" cy="14" r="12" fill="none" stroke="var(--ribbon-red)" stroke-width="3"/><circle cx="14" cy="14" r="6" fill="none" stroke="var(--ribbon-red)" stroke-width="3"/><circle cx="14" cy="14" r="2" fill="var(--ribbon-red)"/></svg>One Hour</li>
      <li><svg viewBox="0 0 28 28" aria-hidden="true"><circle cx="14" cy="14" r="12" fill="none" stroke="var(--ribbon-red)" stroke-width="3"/><circle cx="14" cy="14" r="6" fill="none" stroke="var(--ribbon-red)" stroke-width="3"/><circle cx="14" cy="14" r="2" fill="var(--ribbon-red)"/></svg>Tours Daily</li>
      <li><svg viewBox="0 0 28 28" aria-hidden="true"><circle cx="14" cy="14" r="12" fill="none" stroke="var(--ribbon-red)" stroke-width="3"/><circle cx="14" cy="14" r="6" fill="none" stroke="var(--ribbon-red)" stroke-width="3"/><circle cx="14" cy="14" r="2" fill="var(--ribbon-red)"/></svg>Meet at Halberton St Station</li>
    </ul>
  </div>
</section>

</body>
</html>
```